Steadfast Helm Leadership Roundtable Circuit Promotion

I'm wanting a single page (for now) website to promote my leadership training. Content would include: basic messaging what Steadfast Helm means, invitation to join the Steadfast Helm Roundtable workshops, have me come speak to them, join me on a leadership getaway, get personal coaching, watch some video links of Rud, then referrals of people saying nice things about Rud, connect to Rud’s personal website to learn more about me. The goal of the page is to 1) get people excited to attend a workshop, hear me speak, coach them, or join me on a getaway trip, 2) educate them in how they can get in control of their own life, and 3) link to my personal site to learn more about me. This is the general idea: https://www.varekquill.com/

Target Market(s)

Business owners or self improvement enthusiasts looking to take their businesses and personal lives to the next level.

Industry/Entity Type

Business Consultant

Coding

Coded - Design and coding required

Number of Pages Required

1 page

Font styles to use
Other font styles liked:
• See uploaded logo

Colors
0392cd

Requirements
Must have
• Fonts and colors that match the logo that was uploaded. Uplifting, inspirational look and feel.
Nice to have
• Similar to: https://www.varekquill.com/ and https://dorianfelsk.com/

```html
<!DOCTYPE html>
<html lang="en">
<head>
<meta charset="utf-8">
<title>Steadfast Helm – Leadership Roundtable Circuit</title>
<link href="https://fonts.googleapis.com/css2?family=Libre+Baskerville:wght@400;700&family=Montserrat:wght@400;500;600;700&display=swap" rel="stylesheet">
<style>
:root{
  --brand:#0392cd;
  --brand-dark:#1f5f95;
  --navy:#1c3c6c;
  --ink:#1d1d1d;
  --muted:#555;
  --soft:#e4f2fb;
  --accent:#58b9ea;
  --white:#fff;
}
*{margin:0;padding:0;box-sizing:border-box}
html,body{width:1200px;height:3942px;overflow:hidden}
body{position:relative;font-family:'Montserrat',sans-serif;color:var(--ink);background:var(--white)}
h1,h2,h3,h4{font-weight:400}
.abs{position:absolute}
.btn{position:absolute;display:flex;align-items:center;justify-content:center;font-family:'Montserrat',sans-serif;font-weight:600;font-size:15px;letter-spacing:.3px;text-decoration:none}
.btn-solid{background:var(--brand);color:var(--white)}
.btn-line{border:2px solid var(--brand);color:var(--brand);background:var(--white)}
.btn-white{background:var(--white);color:var(--brand)}

/* hero */
.hero{left:0;top:0;width:1200px;height:620px;background:linear-gradient(100deg,#1d5a86 0%,#3a7595 40%,#5b8fa3 65%,#86acb8 100%)}
.hero-photo{left:640px;top:70px;width:480px;height:500px;background:linear-gradient(160deg,rgba(60,72,88,.15) 0%,rgba(40,48,60,.55) 45%,rgba(28,34,44,.75) 75%,rgba(60,80,100,.2) 100%);border-radius:240px 240px 0 0}
.logo{left:88px;top:30px;color:var(--white);font-family:'Libre Baskerville',serif;font-size:22px;letter-spacing:1px}
.nav{left:505px;top:29px;display:flex;gap:23px;color:var(--white);font-size:12px;font-weight:500;letter-spacing:.5px}
.search{left:1087px;top:27px}
.hero h1{left:88px;top:160px;color:var(--white);font-family:'Libre Baskerville',serif;font-weight:700;font-size:60px;line-height:75px;letter-spacing:2px}
.hero-text{left:88px;top:318px;width:510px;color:var(--white);font-size:16.5px;line-height:25px}
.hero .btn{left:88px;top:427px;width:192px;height:52px;font-size:15px}

/* means */
.section-title{font-family:'Libre Baskerville',serif;text-align:center;color:var(--ink);letter-spacing:1px}
.means-title{left:0;top:630px;width:1200px;font-size:39px}
.means-text{left:320px;top:700px;width:560px;text-align:center;color:var(--muted);font-size:14.5px;line-height:25px;letter-spacing:.4px}

/* workshops */
.handshake{left:0;top:815px;width:1200px;height:718px;background:linear-gradient(110deg,#1e5d93 0%,#2f78ad 40%,#276aa0 70%,#1b5a8c 100%)}
.panel{left:116px;top:1043px;width:966px;height:960px;background:#f2f6f9;box-shadow:0 6px 20px rgba(0,0,0,.12)}
.panel-title{left:116px;top:1088px;width:966px;font-size:40px}
.panel-sub{left:260px;top:1168px;width:680px;text-align:center;color:#333;font-size:16px;line-height:25px;letter-spacing:.4px}
.event{left:143px;width:695px;height:197px;background:var(--white);box-shadow:0 4px 12px rgba(0,0,0,.12)}
.event-photo{position:absolute;left:0;top:0;width:259px;height:197px}
.event-body{position:absolute;left:306px;top:24px;width:360px}
.event-body h3{font-size:15.5px;font-weight:600;margin-bottom:14px}
.event-body p{font-size:12px;color:#888;line-height:14px;margin-bottom:16px}
.event-body dl{font-size:11.5px;line-height:26px}
.event-body dt{display:inline;font-weight:700;color:var(--ink)}
.event-body dd{display:inline;color:#888;margin-left:4px}
.event-actions .btn{width:158px;height:52px;left:882px}

/* focus */
.focus-title{left:88px;top:2150px;width:450px;font-size:38px;line-height:56px;font-family:'Libre Baskerville',serif;letter-spacing:1px}
.focus-text{left:88px;top:2277px;width:420px;font-size:16.5px;line-height:23px;color:#444;letter-spacing:.3px}
.focus .btn{left:88px;top:2446px;width:202px;height:54px}
.frame{background:var(--accent)}
.focus-photo{left:569px;top:2090px;width:527px;height:547px;background:linear-gradient(135deg,#e87a30 0%,#f0b040 28%,#d7c3d8 52%,#6f7fb8 74%,#26345c 100%)}

/* getaway */
.getaway-bg{left:0;top:2695px;width:1200px;height:572px;background:var(--soft)}
.getaway-photo{left:0;top:2695px;width:583px;height:572px;background:linear-gradient(90deg,#7d9a78 0%,#b9c8ba 28%,#e3e8e8 55%,#cfd6db 100%)}
.getaway-title{left:638px;top:2838px;font-size:40px;font-family:'Libre Baskerville',serif;letter-spacing:1px}
.getaway-text{left:638px;top:2915px;width:470px;font-size:16.5px;line-height:26.5px;color:#222;letter-spacing:.3px}
.getaway .btn{left:638px;top:3095px;width:202px;height:54px}

/* testimonials */
.say-title{left:0;top:3318px;width:1200px;font-size:40px}
.quote{background:var(--white);box-shadow:0 4px 16px rgba(0,0,0,.12)}
.quote p{font-size:11px;line-height:21px;color:#444}
.quote.center p{font-size:14px;line-height:27px}
.avatar{border-radius:50%;background:radial-gradient(circle at 50% 40%,#d0b09a 0%,#9a7a66 70%)}

/* footer */
.footer{left:0;top:3655px;width:1200px;height:287px;background:linear-gradient(180deg,#1d3f73,#21457b)}
.fcol{top:3705px;color:#c8d3e4;font-family:'Libre Baskerville',serif;font-size:12.5px;line-height:24px}
.fcol h4{color:var(--white);font-size:14px;margin-bottom:6px;letter-spacing:.3px}
.frule{left:88px;top:3888px;width:1024px;height:1px;background:rgba(255,255,255,.35)}
.social{top:3912px;width:20px;height:20px;background:var(--white);border-radius:3px}
.copy{right:88px;top:3913px;color:var(--white);font-family:'Libre Baskerville',serif;font-size:12px}
</style>
</head>
<body>

<section class="hero abs">
  <div class="hero-photo abs" role="img" aria-label="Portrait of the coach seated in a leather office chair"></div>
  <div class="logo abs">Steadfast Helm</div>
  <nav class="nav abs"><span>ABOUT</span><span>HELP ME WITH</span><span>WORKSHOPS</span><span>RESOURCES</span><span>COACHING</span><span>MISSION</span></nav>
  <svg class="search abs" width="20" height="20" viewBox="0 0 20 20"><circle cx="8" cy="8" r="6.5" fill="none" stroke="#fff" stroke-width="1.8"/><line x1="13" y1="13" x2="18.5" y2="18.5" stroke="#fff" stroke-width="1.8"/></svg>
  <h1 class="abs">MASTERMINDS<br>ARE TRAINED</h1>
  <p class="hero-text abs">We provide business leaders coaching and mentoring in a workshop series. We help them get control of their business and scale up for world domination!</p>
  <a class="btn btn-white">START HERE</a>
</section>

<div class="handshake abs" role="img" aria-label="Blue-toned photo of two business people shaking hands"></div>

<svg class="abs" style="left:0;top:530px" width="1200" height="370" viewBox="0 0 1200 370">
  <path d="M0 70 Q600 -80 1200 70 L1200 290 Q600 440 0 290 Z" fill="#fff"/>
</svg>

<section class="means">
  <h2 class="section-title means-title abs">Steadfast Helm Means</h2>
  <p class="means-text abs">Lorem Ipsum is simply dummy text of the printing and typesetting industry. Lorem Ipsum has been the industry's standard dummy text ever since the 1500s, when an unknown printer took a galley of type and scrambled it to make a type specimen book.</p>
</section>

<section class="workshops">
  <div class="panel abs"></div>
  <h2 class="section-title panel-title abs">Invitation to Join Workshops</h2>
  <p class="panel-sub abs">The ultimate chance to meet the experts this session. You are invited by Steadfast Helm to attend the mastermind workshops.</p>

  <article class="event abs" style="top:1256px">
    <div class="event-photo" role="img" aria-label="Seminar room with folding chairs and a flip chart" style="background:linear-gradient(135deg,#d8d3cb,#a9774f 70%,#8a5a38)"></div>
    <div class="event-body"><h3>Lorem Ipsum</h3><p>Lorem Ipsum is simply dummy text of the printing and typesetting industry.</p>
      <dl><dt>DATE :-</dt><dd>20 - JULY - 2019</dd><br><dt>TIME :-</dt><dd>11:15 am</dd><br><dt>VENUE :-</dt><dd>XYZ</dd></dl></div>
  </article>
  <article class="event abs" style="top:1501px">
    <div class="event-photo" role="img" aria-label="Meeting room with long wooden tables and tall windows" style="background:linear-gradient(135deg,#3d4d6e,#b58a62 60%,#7a4c2e)"></div>
    <div class="event-body"><h3>Lorem Ipsum</h3><p>Lorem Ipsum is simply dummy text of the printing and typesetting industry.</p>
      <dl><dt>DATE :-</dt><dd>28 - JULY - 2019</dd><br><dt>TIME :-</dt><dd>11:15 am</dd><br><dt>VENUE :-</dt><dd>XYZ</dd></dl></div>
  </article>
  <article class="event abs" style="top:1746px">
    <div class="event-photo" role="img" aria-label="Formal council chamber with rows of seats" style="background:linear-gradient(135deg,#e2e6ea,#8a8f98 55%,#5a3e2c)"></div>
    <div class="event-body"><h3>Lorem Ipsum</h3><p>Lorem Ipsum is simply dummy text of the printing and typesetting industry.</p>
      <dl><dt>DATE :-</dt><dd>12 - AUGUST - 2019</dd><br><dt>TIME :-</dt><dd>11:15 am</dd><br><dt>VENUE :-</dt><dd>XYZ</dd></dl></div>
  </article>

  <div class="event-actions">
    <a class="btn btn-solid" style="top:1288px">Registration</a>
    <a class="btn btn-line" style="top:1366px">Know More</a>
    <a class="btn btn-solid" style="top:1533px">Registration</a>
    <a class="btn btn-line" style="top:1611px">Know More</a>
    <a class="btn btn-solid" style="top:1783px">Registration</a>
    <a class="btn btn-line" style="top:1861px">Know More</a>
  </div>
</section>

<section class="focus">
  <h2 class="focus-title abs">Focus On Leadership<br>Grow Your Business</h2>
  <p class="focus-text abs">Lorem Ipsum is simply dummy text of the printing and typesetting industry. Lorem Ipsum has been the industry's standard dummy text ever since the 1500s, when an unknown printer took a galley of type and scrambled it to make</p>
  <a class="btn btn-solid">Know More</a>
  <div class="frame abs" style="left:930px;top:2076px;width:182px;height:182px"></div>
  <div class="frame abs" style="left:553px;top:2468px;width:182px;height:182px"></div>
  <div class="focus-photo abs" role="img" aria-label="Coach speaking at a conference podium in front of a projected slide"></div>
</section>

<section class="getaway">
  <div class="getaway-bg abs"></div>
  <div class="getaway-photo abs" role="img" aria-label="Coach standing in a grey suit beside a bright window"></div>
  <svg class="abs" style="left:0;top:2660px" width="1200" height="60" viewBox="0 0 1200 60"><path d="M0 35 L583 60 L1200 0 L0 0 Z" fill="#fff"/></svg>
  <h2 class="getaway-title abs">A Leadership Getaway</h2>
  <p class="getaway-text abs">Lorem Ipsum is simply dummy text of the printing and typesetting industry. Lorem Ipsum has been the industry's standard dummy text ever since the 1500s, when an unknown printer took a galley of type and scrambled it to make a type specimen book.</p>
  <a class="btn btn-solid">Know More</a>
</section>

<section class="testimonials">
  <h2 class="section-title say-title abs">What People Says About Us</h2>
  <div class="quote abs" style="left:181px;top:3430px;width:234px;height:140px;padding:38px 0 0 32px"><p>It's our Commitment to providing truthful, authentic information regarding your legal needs and concers.<br>"Marlow Trent"</p></div>
  <div class="quote abs" style="left:785px;top:3430px;width:210px;height:140px;padding:38px 18px 0 0;text-align:right"><p>It's our Commitment to providing truthful, authentic information regarding your legal needs and concers.<br>"Marlow Trent"</p></div>
  <div class="quote center abs" style="left:413px;top:3402px;width:375px;height:210px;padding:50px 40px 0"><p>It's our Commitment to providing truthful, authentic information regarding your legal needs and concers.<br><br>"Marlow Trent"</p></div>
  <div class="avatar abs" role="img" aria-label="Client portrait" style="left:301px;top:3405px;width:46px;height:46px"></div>
  <div class="avatar abs" role="img" aria-label="Client portrait" style="left:565px;top:3375px;width:58px;height:58px"></div>
  <div class="avatar abs" role="img" aria-label="Client portrait" style="left:818px;top:3405px;width:46px;height:46px"></div>
</section>

<footer class="footer abs"></footer>
<div class="fcol abs" style="left:88px"><h4>GET IN TOUCH</h4>EMAIL :<br>steadfasthelm.example<br>CONTACT :<br>+ 1555 010 246</div>
<div class="fcol abs" style="left:325px"><h4>ADDRESS</h4>B7, 40-62 Larkfield Lane North<br>Vale, 318<br>Steadfast Helm Pvt.Ltd<br>XYZ 55 555 55 55</div>
<div class="fcol abs" style="left:619px;width:210px;line-height:21px"><h4>MOBILE INQURIES</h4>It is a long established fact that a reader will be distracted by the readable content of a page when looking at its layout.</div>
<div class="fcol abs" style="left:908px;width:210px;line-height:21px"><h4>CUSTOMER SUPPORT</h4>It is a long established fact that a reader will be distracted by the readable content of a page when looking at its layout.</div>
<div class="frule abs"></div>
<div class="social abs" style="left:98px"></div>
<div class="social abs" style="left:142px"></div>
<div class="social abs" style="left:180px"></div>
<div class="social abs" style="left:218px"></div>
<div class="copy abs">Copyrights © 2019 - Steadfast Helm. All Rights Reserved</div>

</body>
</html>
```